Flyer Design for a Mediation (Rediation on Quiet Rivers)

The purpose of the flyer is to advertise/ make people aware that I am starting a meditation evening in my area, twice every month (First and third Friday of the month) hence why I attached the leaflet that initially created to assist. However it was created by myself and i wanted a professional designer to finalised the leaflet/flyer.

I would like a 2 sided leaflet.
Front of leaflet

1) TOP BANNER
# Banner to be Royal Blue (a darker royal blue)
#Must have a fine gold line at the bottom of the top banner
# Wording "Velmoric Tending " must be in one line and below the word “Harrowick” all to be in gold. Please note that wording must be placed to the far left hand side.
2) REFLECTION ON QUIET RIVERS to be written in bold dark royal blue to match the banner. This is to be placed to the centre of the page.
Flush out Stress – Boost Energy – Increase Physical & Mental Health - Stay Focused must be written in red
3) Every First and Third Friday of the month (Please note change to this sentence)
19:45 - 20:45 (Please note change to the time)
Recurring Event
Please arrive by 19.30 for a brief introduction .

4) Our guided Mediation is for over 18’s only. Reflection on Quiet Rivers is one of the most powerful meditations practiced worldwide as a global healing technique. (the wording “Reflection on Quiet Rivers” in this sentence, must be in Gold)

5) The following details to be added to the first page:
Eastmere Reading House
Meeting Room
42 Pellow Market Row, Harrowick, DA3 7QJ
Mobile: 079 4620 7158
Email: eastmerevelmorictend@brivelmail.net
Like us on Facebook: Eastmere Velmic Tending
6) Rediation on Quiet Rivers is one of the most powerful mediation tools for spiritual development. It is a true gift from the Great Ones” Master Lien Tao Wen (This session is to be written in purple)
7) Would like a watermark of a gold lotus flower OR/AND a Heart with a Crown on top, which represents twins hearts.

Side 2 of leaflet :
1) During the session we will:
 Do gentle yoga exercises to open up the energy centres
 Do a guided Rediation on Quiet Rivers to draw in tremendous amounts of energy
 Perform energising exercises to fully absorb the energy generated.

2) We do not charge for the evening but ask for a donation. (This sentence must be in Red)

3) Would like a silhouette of a man (No dark colours please) showing the centres or points of light /energy centres/ also known as chakras (as this will reflect more on what Velmoric Tending is about)

Thank you very much

Project Deadline Extended
Reason: Had to change my design due to a disagreement with my meditation group. Mediation wording and images had to be changed. I have all information. Would like to extend deadline until Sunday07th June 2015 if possible. Thank you and please advise if there are any further charges. Once again my sincere apologises.

Target Market(s)

Everyone interested in spirituality/meditation

Font styles to use
Decorative
Other font styles liked:
• ARIAL

Colors
0455a3
ffc214
6b449b
ffffff

Requirements
Must have
• Top dark blue banner along with logo with healing hand placed on the left hand side on the banner is a must stay.
Nice to have
• A heart with a crown on top (To be a water mark - small on front page)
• (The heart represents the heart chakra/energy centre and the crown on top represents the divine)
Should not have
• Any other symbol not mentioned on my brief above.

```html
<!DOCTYPE html>
<html lang="en">
<head>
<meta charset="utf-8">
<title>Velmoric Tending Harrowick – Reflection on Quiet Rivers Leaflet</title>
<link rel="stylesheet" href="https://fonts.googleapis.com/css2?family=Delius&family=Questrial&family=Poiret+One&family=Open+Sans:wght@400;600;700&family=Montserrat:wght@800&display=swap">
<style>
  :root {
    --page-grey: #c6c6c6;
    --navy: #1f1c5b;
    --gold: #f7bf16;
    --red: #e02a2a;
    --lavender: #7b5fae;
    --purple: #6b449b;
    --white: #ffffff;
    --card-shadow: 6px 8px 8px rgba(0,0,0,0.45);
  }
  * { box-sizing: border-box; margin: 0; padding: 0; }
  html, body { width: 850px; height: 1200px; overflow: hidden; }
  body { background: var(--page-grey); position: relative; font-family: Arial, Helvetica, sans-serif; }

  .leaflet-side { position: absolute; left: 47px; width: 748px; box-shadow: var(--card-shadow); overflow: hidden; }

  /* Front */
  .front { top: 27px; height: 525px; background: var(--white); }
  .top-banner { position: absolute; left: 0; top: 0; width: 100%; height: 77px; background: var(--navy); }
  .gold-rule { position: absolute; left: 0; top: 77px; width: 100%; height: 6px; background: var(--gold); }
  .logo-image { position: absolute; left: 3px; top: 3px; width: 72px; height: 72px;
    background: radial-gradient(circle at 55% 50%, #9fe4ff 0%, #2d7fc6 35%, #0a1a3a 75%); }
  .brand-name { position: absolute; right: 38px; top: 15px; text-align: right; color: var(--gold);
    font-family: Arial, Helvetica, sans-serif; font-weight: 700; font-size: 20px; line-height: 25px; }

  .lotus-watermark { position: absolute; left: 150px; top: 110px; width: 450px; height: 340px;
    background: radial-gradient(ellipse at 50% 60%, rgba(247,191,22,0.16) 0%, rgba(247,191,22,0.08) 45%, rgba(255,255,255,0) 70%); }

  .event-title { position: absolute; left: 0; width: 100%; top: 97px; text-align: center; color: var(--navy);
    font-family: "Montserrat", Arial, sans-serif; font-weight: 800; font-size: 25px; letter-spacing: 0.3px; }
  .benefits { position: absolute; left: 0; width: 100%; top: 135px; text-align: center; color: var(--red);
    font-family: "Delius", cursive; font-size: 27px; line-height: 33px; }

  .schedule-band { position: absolute; left: 0; top: 210px; width: 100%; height: 46px; background: var(--navy);
    color: var(--white); text-align: center; font-family: "Open Sans", Arial, sans-serif; font-weight: 600;
    font-size: 20px; line-height: 46px; }

  .arrival-note { position: absolute; left: 0; width: 100%; top: 263px; text-align: center; color: var(--navy);
    font-size: 13.5px; line-height: 18px; }
  .intro { position: absolute; left: 0; width: 100%; top: 310px; text-align: center; color: var(--lavender);
    font-family: "Delius", cursive; font-size: 17.5px; line-height: 23px; }
  .intro .highlight { color: var(--gold); }

  .contact-details { position: absolute; left: 38px; top: 382px; color: var(--navy); font-style: normal;
    font-family: "Questrial", Arial, sans-serif; font-size: 14px; line-height: 18.5px; text-transform: uppercase; }

  .lotus-emblem { position: absolute; left: 350px; top: 433px; width: 120px; height: 62px;
    background: radial-gradient(ellipse at 50% 80%, #8f5fc0 0%, #b493dc 45%, rgba(255,255,255,0) 72%); }

  .teacher-quote { position: absolute; right: 38px; top: 397px; width: 232px; text-align: right; color: var(--purple);
    font-family: "Delius", cursive; font-size: 12.5px; line-height: 16px; white-space: nowrap; }

  /* Back */
  .back { top: 640px; height: 527px; }
  .session-photo { position: absolute; inset: 0;
    background:
      radial-gradient(ellipse at 72% 55%, #e9e1dc 0%, #cbb6b0 22%, rgba(120,70,130,0) 48%),
      linear-gradient(100deg, #2a0f33 0%, #4a1f5c 40%, #6a3f7c 62%, #efeaf0 95%); }
  .session-heading { position: absolute; left: 44px; top: 42px; color: var(--white);
    font-family: "Poiret One", sans-serif; font-weight: 400; font-size: 38px; }
  .session-steps { position: absolute; left: 50px; top: 128px; width: 290px; list-style: none; color: var(--white);
    font-family: "Open Sans", Arial, sans-serif; font-size: 18.5px; line-height: 24px; }
  .session-steps li { position: relative; padding-left: 23px; margin-bottom: 24px; white-space: nowrap; }
  .session-steps li::before { content: ""; position: absolute; left: 0; top: 9px; width: 8px; height: 8px;
    border-radius: 50%; background: var(--white); }
  .donation-note { position: absolute; left: 46px; top: 474px; color: var(--red);
    font-family: "Open Sans", Arial, sans-serif; font-weight: 700; font-size: 16px; }
  .chakra-figure { position: absolute; left: 611px; top: 396px; width: 115px; height: 112px;
    background: radial-gradient(circle at 50% 45%, #ffffff 0%, #c9b2ec 35%, #7b4fb8 80%); }
</style>
</head>
<body>

<section class="leaflet-side front">
  <div class="top-banner"></div>
  <div class="gold-rule"></div>
  <div class="logo-image" role="img" aria-label="Healing hand emitting light"></div>
  <div class="brand-name">Velmoric Tending<br>Harrowick</div>

  <div class="lotus-watermark" role="img" aria-label="Faint gold lotus flower watermark"></div>

  <h1 class="event-title">REFLECTION ON QUIET RIVERS</h1>
  <p class="benefits">flush out stress &nbsp;.&nbsp; boost energy &nbsp;. stay focused<br>increase physical and mental strength</p>

  <div class="schedule-band">Every First and Third Friday of the month 19:45 - 20:45</div>

  <p class="arrival-note">Recurring Event - Please arrive by 7.15 pm for a brief introduction.<br>Our guided Mediation is for over 18's only.</p>

  <p class="intro">All are welcome to come to a guided Mediation. <span class="highlight">Reflection on Quiet Rivers</span> is one of<br>most powerful meditations, practiced worldwide as a global healing technique.</p>

  <address class="contact-details">
    Eastmere Reading House - Meeting Room<br>
    42 Pellow Market Row, Harrowick DA3 7QJ<br>
    kent.velmorictend@brivelmail.net<br>
    Mobile: 079 4620 7158<br>
    eastmerevelmorictend@brivelmail.net<br>
    Facebook: Eastmere Velmic Tending6)
  </address>

  <div class="lotus-emblem" role="img" aria-label="Purple lotus flower"></div>

  <p class="teacher-quote">"Reflection on Quiet Rivers is one of<br>the most powerful meditation tools<br>for spiritual development. It is a<br>true gift from the great ones"<br>Master Lien Tao Wen</p>
</section>

<section class="leaflet-side back">
  <div class="session-photo" role="img" aria-label="Person seated cross-legged in meditation on a purple background"></div>
  <h2 class="session-heading">During the session we will:</h2>
  <ul class="session-steps">
    <li>Do gentle yoga exercises<br>to open up the energy<br>centres.</li>
    <li>Do a guided mediation on<br>Quiet Rivers to draw in<br>tremendous amounts of<br>energy.</li>
    <li>Perform energising<br>exercises to fully absorb<br>the energy generated.</li>
  </ul>
  <p class="donation-note">We do not charge for the evening but ask for a donation.</p>
  <div class="chakra-figure" role="img" aria-label="Seated silhouette with glowing chakra points"></div>
</section>

</body>
</html>
```